Stationary or Corporate Identity package for small Software Development Company

I have a logo and am looking for letterhead, envelope, and possibly business card design. Letterhead and envelope can use all images from the attached business card or open to other ideas that can incorporate the logo. Looking for colorful design to grab attention. Also wanting a more Professional look and less whimsical with maybe a little on the bolder side (maybe more of the masculine side?) Definitely a more modern look over a boring traditional look.

Target Market(s)

Clients are IT Recruiters and IT/Software Staffing and Consulting companies

Industry/Entity Type

Computer Software

Font styles to use
Sans Serif

Requirements
Must have
• Must have the logo, and places for address information, phone number, email, and website information. Colors should coordinate with logo.
Nice to have
• I like the look where there is a semi-transparent abstract image or part of the logo that sort of swooshes in from the left side of the paper. This is not necessary if other good ideas come to mind. Would like a little bit of color to the stationary and envelope, not just a header/footer type with just the logo and a colored separation line.

```html
<!DOCTYPE html>
<html lang="en">
<head>
<meta charset="utf-8">
<title>Quorvex Stationery</title>
<link rel="stylesheet" href="https://fonts.googleapis.com/css2?family=Ubuntu:wght@300;700&family=Arimo:wght@400;700&display=swap">
<style>
:root{
  --backdrop:#d3d3d3;
  --paper:#f1f1f1;
  --ink:#1e1e1e;
  --charcoal:#262626;
  --navy:#0b2a6b;
  --sky:#3fb0e0;
  --orange:#f39a10;
  --red:#e80a0a;
  --muted:#555;
  --icon:#2ea84a;
}
*{margin:0;padding:0;box-sizing:border-box}
html,body{width:1200px;height:1041px;overflow:hidden;background:var(--backdrop)}
.canvas{position:relative;width:1200px;height:1041px;font-family:Arimo,Arial,sans-serif;color:var(--ink)}
.sheet{position:absolute;background:var(--paper);box-shadow:0 1px 3px rgba(0,0,0,.18);overflow:hidden}
.artwork{position:absolute;inset:0;background:linear-gradient(135deg,var(--orange) 0%,var(--red) 70%,var(--charcoal) 100%)}
.faint-art{position:absolute;top:0;right:0;background:linear-gradient(90deg,rgba(226,226,226,0),rgba(226,226,226,.8))}
.brand-mark{position:absolute;border-radius:50%;background:var(--red)}
.brand-name{position:absolute;font-family:Ubuntu,Arial,sans-serif;font-weight:700;color:var(--ink);line-height:1;white-space:nowrap}
.tagline{position:absolute;font-family:Ubuntu,Arial,sans-serif;font-weight:300;color:var(--muted);white-space:nowrap;line-height:1}
.footer-band{position:absolute;left:0;right:0;bottom:0;border-top:2px solid var(--navy);background:linear-gradient(90deg,var(--navy) 0%,var(--sky) 35%,var(--orange) 60%,var(--red) 100%)}
.contact{position:absolute;font-size:5.5px;line-height:7px;color:#333;white-space:nowrap}
.contact .ico{display:inline-block;width:4px;height:4px;border-radius:1px;background:var(--icon);margin-right:3px;vertical-align:middle}

/* folder */
.folder{left:166px;top:76px;width:418px;height:541px;border-radius:3px}
.folder .spine{position:absolute;left:26px;top:0;bottom:0;width:2px;background:rgba(0,0,0,.12)}
.folder .brand-mark{left:251px;top:389px;width:56px;height:56px;background:#fff}
.folder .brand-name{left:217px;top:454px;font-size:30px;color:#fff}
.folder .tagline{left:242px;top:487px;font-size:12px;color:#fff}

/* letterhead */
.letterhead{left:615px;top:95px;width:403px;height:522px}
.letterhead .faint-art{width:190px;height:300px}
.letterhead .brand-mark{left:38px;top:28px;width:44px;height:44px}
.letterhead .brand-name{left:30px;top:78px;font-size:20px}
.letterhead .tagline{left:48px;top:99px;font-size:5px}
.letterhead .contact{left:315px;top:40px}
.letterhead .footer-band{height:8px}

/* envelope front */
.env-front{left:132px;top:645px;width:451px;height:196px}
.env-front .faint-art{width:220px;height:170px}
.env-front .brand-mark{left:36px;top:24px;width:44px;height:44px}
.env-front .brand-name{left:26px;top:74px;font-size:20px}
.env-front .tagline{left:44px;top:95px;font-size:5px}
.env-front .contact{left:29px;top:160px;text-align:center}
.env-front .footer-band{height:7px}

/* envelope back */
.env-back{left:615px;top:645px;width:451px;height:196px}
.env-back .flap{position:absolute;left:0;top:0;width:451px;height:66px}
.env-back .brand-mark{left:215px;top:20px;width:22px;height:22px}
.env-back .contact{left:0;width:451px;top:171px;text-align:center;font-size:4.5px}

/* business cards */
.card-front{left:418px;top:872px;width:164px;height:91px;border-radius:4px}
.card-front .brand-mark{left:33px;top:17px;width:28px;height:28px}
.card-front .brand-name{left:27px;top:50px;font-size:13px}
.card-front .divider{position:absolute;left:84px;top:22px;width:1px;height:40px;background:#cfcfcf}
.card-front .person{position:absolute;left:94px;top:21px;font-size:5.5px;font-weight:700;line-height:7px}
.card-front .role{position:absolute;left:94px;top:28px;font-size:4px;color:#555}
.card-front .contact{left:94px;top:36px;font-size:4px;line-height:5.5px}
.card-front .contact .ico{width:3px;height:3px}
.card-front .footer-band{height:4px;border-top-width:1px}
.card-back{left:616px;top:872px;width:165px;height:91px;border-radius:4px}
.card-back .brand-mark{left:60px;top:18px;width:32px;height:32px;background:#fff}
.card-back .brand-name{left:52px;top:56px;font-size:14px;color:#fff}
.card-back .tagline{left:63px;top:72px;font-size:5.5px;color:#fff}
</style>
</head>
<body>
<main class="canvas">

  <section class="sheet folder">
    <div class="artwork" role="img" aria-label="Abstract artwork of sweeping colour bands in yellow, orange, red, black, blue and green"></div>
    <div class="spine"></div>
    <span class="brand-mark"></span>
    <span class="brand-name">Quorvex</span>
    <span class="tagline">Software Development</span>
  </section>

  <section class="sheet letterhead">
    <div class="faint-art" role="img" aria-label="Faint abstract decoration"></div>
    <span class="brand-mark"></span>
    <span class="brand-name">Quorvex</span>
    <span class="tagline">Software Development</span>
    <div class="contact">
      <div><span class="ico"></span>555-014-2290</div>
      <div><span class="ico"></span>info@quorvex.com</div>
      <div><span class="ico"></span>www.quorvex.com</div>
      <div style="margin-top:3px">42 Alder Lane,</div>
      <div>Millbrook, OH 44201</div>
    </div>
    <div class="footer-band"></div>
  </section>

  <section class="sheet env-front">
    <div class="faint-art" role="img" aria-label="Faint abstract decoration"></div>
    <span class="brand-mark"></span>
    <span class="brand-name">Quorvex</span>
    <span class="tagline">Software Development</span>
    <div class="contact"><div>42 Alder Lane,</div><div>Millbrook, OH 44201</div></div>
    <div class="footer-band"></div>
  </section>

  <section class="sheet env-back">
    <svg class="flap" viewBox="0 0 451 66" aria-hidden="true">
      <path d="M0 0 H451 L436 60 Q434 64 428 64 H23 Q17 64 15 60Z" fill="#262626"/>
    </svg>
    <span class="brand-mark"></span>
    <div class="contact">www.quorvex.com</div>
  </section>

  <section class="sheet card-front">
    <span class="brand-mark"></span>
    <span class="brand-name">Quorvex</span>
    <span class="divider"></span>
    <span class="person">JORDAN HALE</span>
    <span class="role">General Manager</span>
    <div class="contact">
      <div><span class="ico"></span>555-014-2290</div>
      <div><span class="ico"></span>info@quorvex.com</div>
      <div><span class="ico"></span>www.quorvex.com</div>
      <div style="margin-top:2px">42 Alder Lane,</div>
      <div>Millbrook, OH 44201</div>
    </div>
    <div class="footer-band"></div>
  </section>

  <section class="sheet card-back">
    <div class="artwork" role="img" aria-label="Abstract artwork of colour bands in yellow, orange, red, black, blue and green"></div>
    <span class="brand-mark"></span>
    <span class="brand-name">Quorvex</span>
    <span class="tagline">Software Development</span>
  </section>

</main>
</body>
</html>
```